Up to the Challenge? Canadian based consulting company needs a two sided business card design

A Canadian based security risk management consulting company needs a two-sided business card design. What we do is provide advice and guidance related to emergency, security and business continuity management for small, medium and large companies to help ensure the protection of their people, assets, information, services, operations and reputation.

The final design should be simple, only one or two colours, eye catching, professional and one that makes people look at three or more times just because it looks so darn good.

I have include examples of business cards I like.

Target Market(s)

Small, medium and large companies.

Industry/Entity Type

Security

Contact Information for Business Card

Business Card Size: Standard size of 3.5" (89mm) x 2.0" (51mm) - (see full specifications and guides on PRINTA's website if required)
Card Stock: Looking to use PRINTA's Velda 32pt stock textured paper - seam colour either chili red or black
Business Name: The Harrowfield Group
Website: www.theharrowfieldgroup.example
Telephone: (555)214-0397
Name: Dana Forsythe
Position: Principle
e-mail: Dana.Forsythe@theharrowfieldgroup.example

Font styles to use
Serif

Colors
ec1f27
000000
9d9d9d
aaaaaa
606060

Requirements
Must have
• - "The Harrowfield Group" logo (see uploaded files). I have included grey scale and colour versions.
• - Business card details (as above)
Nice to have
• - One side black or grey scale.
• - Other side would likely be white.
• - Everyone likes the silver logo on the black background.
• - Small element of colour i.e. red but I'm leaning more to greyscale.
Should not have
• - A lot of colour. Keep it simple.

```html
<!DOCTYPE html>
<html lang="en">
<head>
<meta charset="utf-8">
<title>The Harrowfield Group — Business Card</title>
<link href="https://fonts.googleapis.com/css2?family=Cinzel:wght@400;600&family=Marcellus+SC&display=swap" rel="stylesheet">
<style>
  :root {
    --page: #e9e7e3;
    --card-black: #0d0d0d;
    --card-white: #ecebe8;
    --silver: #9d9d9d;
    --silver-light: #aaaaaa;
    --ink: #1a1a1a;
    --ink-mid: #606060;
    --leaf-dark: #7c7c7c;
    --leaf-light: #b3b3b3;
  }
  * { margin: 0; padding: 0; box-sizing: border-box; }
  html, body {
    width: 1200px;
    height: 918px;
    overflow: hidden;
    background: var(--page);
  }
  .canvas {
    position: relative;
    width: 1200px;
    height: 918px;
  }
  .card {
    position: absolute;
    left: 340px;
    width: 520px;
    height: 297px;
    box-shadow: 0 6px 18px rgba(0,0,0,0.18);
  }
  /* Back side */
  .card-back {
    top: 130px;
    background: var(--card-black);
  }
  .card-back .frame {
    position: absolute;
    inset: 14px;
    border: 2px solid var(--ink-mid);
  }
  .brand {
    position: absolute;
    inset: 0;
    display: flex;
    align-items: center;
    justify-content: center;
    gap: 14px;
  }
  .brand-mark {
    width: 30px;
    height: 30px;
    background: var(--ink-mid);
  }
  .brand-name {
    font-family: "Cinzel", serif;
    font-weight: 600;
    font-size: 26px;
    letter-spacing: 2px;
    color: var(--ink-mid);
    text-align: center;
    line-height: 1.15;
  }
  /* Front side */
  .card-front {
    top: 491px;
    background: var(--card-white);
    overflow: hidden;
  }
  .tree-art {
    position: absolute;
    left: 0;
    top: 18px;
    width: 215px;
    height: 279px;
    background: radial-gradient(ellipse at 45% 40%, var(--leaf-light), var(--leaf-dark) 75%);
    border-radius: 0 50% 0 0;
    opacity: 0.85;
  }
  .contact {
    position: absolute;
    right: 24px;
    top: 110px;
    text-align: right;
    font-family: "Marcellus SC", serif;
    color: var(--ink);
  }
  .contact .person {
    font-family: "Cinzel", serif;
    font-size: 22px;
    letter-spacing: 1px;
    line-height: 1.1;
  }
  .contact .role {
    font-family: "Cinzel", serif;
    font-size: 15px;
    margin-bottom: 4px;
  }
  .contact .line {
    font-size: 13.5px;
    line-height: 1.65;
    letter-spacing: 0.3px;
  }
</style>
</head>
<body>
<div class="canvas">
  <section class="card card-back" aria-label="Card back">
    <div class="frame"></div>
    <div class="brand">
      <span class="brand-mark"></span>
      <span class="brand-name">THE HARROWFIELD<br>GROUP</span>
    </div>
  </section>

  <section class="card card-front" aria-label="Card front">
    <div class="tree-art" role="img" aria-label="Large grey illustration of a young tree with leaves"></div>
    <div class="contact">
      <p class="person">DANA FORSYTHE</p>
      <p class="role">PRINCIPLE</p>
      <p class="line">www.theharrowfieldgroup.example</p>
      <p class="line">P: (555)214-0397</p>
      <p class="line">Dana.Forsythe@theharrowfieldgroup.example</p>
      <p class="line">Dana.Forsythe@theharrowfieldgroup.example</p>
    </div>
  </section>
</div>
</body>
</html>
```